Horse related business entrepreneur needs a business card

I need a business card design for my horse related business. The enterprise is Tall Fern LLC and I have 3 businesses (headquartered at 2 locations): 1. property management where we rent horse stalls and apartments at a thoroughbred training center outside Ocala; 2. a medium sized transportation service in central Florida that sells horse bedding and removes used horse bedding from horse farms; and horse racing

```html
<!DOCTYPE html>
<html lang="en">
<head>
<meta charset="utf-8">
<title>Tall Fern LLC – Business Card</title>
<link href="https://fonts.googleapis.com/css2?family=Tinos:wght@400;700&display=swap" rel="stylesheet">
<style>
  :root {
    --page-bg: #e6e4e3;
    --card-white: #ffffff;
    --card-maroon: #3c2429;
    --ink-maroon: #3f1e25;
    --ink-light: #f4eeee;
    --ink-soft: #e2d6d7;
    --shadow: rgba(40, 20, 25, 0.18);
  }
  * { box-sizing: border-box; margin: 0; padding: 0; }
  html, body {
    width: 800px; height: 1200px; overflow: hidden;
    background: var(--page-bg);
    font-family: "Tinos", "Times New Roman", serif;
  }
  .sheet {
    width: 800px; height: 1200px;
    display: flex; flex-direction: column; align-items: center; justify-content: center;
    gap: 110px;
  }
  .card {
    width: 640px; height: 366px;
    border-radius: 26px;
    box-shadow: 0 10px 30px var(--shadow);
    position: relative;
  }
  .card--front { background: var(--card-white); color: var(--ink-maroon); }
  .card--back { background: var(--card-maroon); color: var(--ink-light); }

  /* Front */
  .contact-block {
    position: absolute; left: 0; right: 0; top: 148px;
    display: flex; justify-content: center; align-items: center; gap: 26px;
  }
  .identity { text-align: right; }
  .identity__name { font-size: 24px; font-weight: 700; line-height: 1.05; }
  .identity__role { font-size: 15px; }
  .divider-v { width: 2px; height: 66px; background: currentColor; }
  .contact-list { list-style: none; font-size: 17px; font-weight: 700; line-height: 1.4; }
  .contact-list li { display: flex; align-items: center; gap: 10px; }
  .contact-list svg { width: 14px; height: 14px; fill: var(--ink-maroon); flex: none; }

  /* Back */
  .brand {
    position: absolute; left: 100px; top: 92px;
    display: flex; align-items: center; gap: 22px;
  }
  .brand__mark { width: 60px; height: 60px; background: var(--ink-light); }
  .brand__name { font-size: 56px; font-weight: 700; letter-spacing: 0.5px; color: var(--ink-light); }
  .locations {
    position: absolute; left: 0; right: 0; top: 230px;
    display: flex; justify-content: center; align-items: center; gap: 26px;
    font-size: 17px; line-height: 1.35; color: var(--ink-soft);
  }
  .locations__item--left { text-align: right; }
  .locations .divider-v { height: 48px; background: var(--ink-soft); }
</style>
</head>
<body>
  <main class="sheet">
    <section class="card card--front" aria-label="Card front">
      <div class="contact-block">
        <div class="identity">
          <p class="identity__name">Owen Hartley</p>
          <p class="identity__role">Owner</p>
        </div>
        <span class="divider-v"></span>
        <ul class="contact-list">
          <li>
            <svg viewBox="0 0 16 16" aria-hidden="true"><path d="M2 5c0-2 2-3 6-3s6 1 6 3v1h-3V5H5v1H2zM4 7h8l2 6H2z"/></svg>
            (555) 210-4187
          </li>
          <li>
            <svg viewBox="0 0 16 16" aria-hidden="true"><path d="M6 2h4v2h4v10H2V4h4zM7 3v1h2V3z"/></svg>
            (555) 210-4390
          </li>
          <li>
            <svg viewBox="0 0 16 16" aria-hidden="true"><path d="M1 3h14v10H1zM2 4l6 5 6-5z" fill-rule="evenodd"/></svg>
            owen@tallfern.com
          </li>
        </ul>
      </div>
    </section>

    <section class="card card--back" aria-label="Card back">
      <div class="brand">
        <span class="brand__mark" aria-hidden="true"></span>
        <h1 class="brand__name">Tall Fern LLC</h1>
      </div>
      <div class="locations">
        <address class="locations__item locations__item--left" style="font-style:normal">
          118 Maple Ridge Lane<br>Greenfield, VA 22900
        </address>
        <span class="divider-v"></span>
        <address class="locations__item" style="font-style:normal">
          742 SE Oakmont Road<br>Fairhaven, FL 32600
        </address>
      </div>
    </section>
  </main>
</body>
</html>
```